Billboard Design for Equipment Rental Business

We need a billboard design for our equipment rental business called Brevard Machinery Company. We are based in Georgia. We rent construction tools, equipment, and dumpsters. We currently have a design but feel like we could get something better. Our phone number is 912-307-5186 and our website is www.brevardmachinery-example.com

```html
<!DOCTYPE html>
<html lang="en">
<head>
<meta charset="utf-8">
<title>Brevard Machinery Company – Billboard</title>
<link rel="stylesheet" href="https://fonts.googleapis.com/css2?family=Montserrat:wght@600;700&display=swap">
<style>
  :root {
    --backdrop: #ececec;
    --sign-yellow: #f8bf24;
    --ink: #373435;
    --art-top: #f3b81c;
    --art-bottom: #e9ad14;
  }
  * { margin: 0; padding: 0; box-sizing: border-box; }
  html, body {
    width: 1152px;
    height: 1200px;
    overflow: hidden;
    background: var(--backdrop);
  }
  .billboard {
    position: absolute;
    left: 26px;
    top: 50px;
    width: 1100px;
    height: 1100px;
    overflow: hidden;
    background: var(--sign-yellow);
    font-family: "Montserrat", Arial, sans-serif;
    color: var(--ink);
  }
  .hero-art {
    position: absolute;
    left: 242px;
    top: 40px;
    width: 615px;
    height: 441px;
    background: linear-gradient(180deg, var(--art-top), var(--art-bottom));
    border-radius: 6px;
  }
  .brand-name,
  .brand-tagline,
  .phone,
  .website {
    position: absolute;
    left: 0;
    width: 100%;
    text-align: center;
    white-space: nowrap;
    line-height: 1;
  }
  .brand-name {
    top: 517px;
    font-size: 172px;
    font-weight: 700;
    letter-spacing: 0;
  }
  .brand-tagline {
    top: 722px;
    font-size: 70px;
    font-weight: 700;
  }
  .phone {
    top: 854px;
    font-size: 114px;
    font-weight: 700;
    letter-spacing: 1px;
  }
  .website {
    top: 1004px;
    font-size: 38px;
    font-weight: 600;
  }
</style>
</head>
<body>
  <main class="billboard">
    <div class="hero-art" role="img" aria-label="Line illustration of a tracked excavator with its arm and bucket raised"></div>
    <h1 class="brand-name">BREVARD</h1>
    <p class="brand-tagline">MACHINERY COMPANY</p>
    <p class="phone">912-307-5186</p>
    <p class="website">www.brevardmachinery-example.com</p>
  </main>
</body>
</html>
```